New Sports Team- Womens Football

New team in San Diego.  Looking for a website that can be updated by us after the design is established.
Pages needed:
About us
Roster
Coaches/Staff
Schedule
Online Store (This link will go out to an external vendor)
Community Partners /Sponsors
Some good team pages to take a look at:
velmaroquills.com
brindlecoveotterball.com

Please use the logo I attempted to upload.  Looking for Flash Intro that incorporates the definition of the word "KESTO" and then the logo appearing.
Use the following words:
;any sudden, strong increase, as of energy, enthusiasm, etc.
;To improve one's performance suddenly, especially in bettering one's standing in a competition.

I placed a couple more pictures.
Adding another version of the team logo. In all designs I have seen thus far, everyone has the logo very small and it appears transparent. Might help to have the jpeg version. Also added some more photos
We are approaching the deadline quickly. Just a few last notes to the designs I have been viewing. All designs that are not close to the brief will be eliminated.

```html
<!DOCTYPE html>
<html lang="en">
<head>
<meta charset="utf-8">
<title>KESTO Women's Football</title>
<link href="https://fonts.googleapis.com/css2?family=Arimo:wght@400;700&display=swap" rel="stylesheet">
<style>
:root{
  --navy-deep:#06173f;
  --navy:#0c2a78;
  --blue:#1646a8;
  --blue-bright:#1e64c8;
  --sky:#5fb8f0;
  --link:#6fc3f5;
  --orange:#f05a14;
  --red-bar:#e8300a;
  --green-bar:#8fcc10;
  --amber-bar:#f5a000;
  --panel-light:#e9eef6;
  --panel-mid:#d6e0ee;
  --ink:#1a1a1a;
  --muted:#8fa6c8;
  --white:#ffffff;
}
*{box-sizing:border-box;margin:0;padding:0}
html,body{width:1137px;height:1200px;overflow:hidden}
body{
  font-family:"Arimo",Arial,sans-serif;
  background:radial-gradient(ellipse at 50% 10%,#1f5fc4 0%,#0f3790 35%,#082160 70%,var(--navy-deep) 100%);
  color:var(--white);
  position:relative;
}
.abs{position:absolute}
/* top bar */
.account-bar{left:0;top:0;width:1137px;height:31px;background:rgba(4,20,60,.45);border-bottom:1px solid rgba(255,255,255,.15)}
.account-link{left:676px;top:9px;font-size:11px;color:var(--link);text-decoration:underline}
.login-field{top:8px;width:92px;height:15px;background:var(--white);border:1px solid #9ab}
.login-btn{left:973px;top:7px;width:44px;height:17px;border-radius:3px;background:linear-gradient(#6cc6f8,#1f86d8);font-size:11px;text-align:center;line-height:17px}
/* brand */
.brand{left:160px;top:30px;display:flex;align-items:center;gap:10px}
.brand-mark{width:26px;height:26px;border-radius:50%;background:var(--white)}
.brand-name{font-size:52px;font-weight:700;color:var(--white);letter-spacing:1px}
.call-us{left:813px;top:50px;font-size:22px;letter-spacing:.5px}
.social{top:89px;width:32px;height:32px;border-radius:5px;background:var(--white);opacity:.9}
/* header panel */
.header-panel{left:123px;top:128px;width:906px;height:345px;border-radius:8px;background:linear-gradient(#eef2f8,#d3dce9)}
.main-nav{left:0;top:0;width:906px;height:35px;display:flex;border-bottom:1px solid #b7c3d4;border-radius:8px 8px 0 0;background:linear-gradient(#fbfcfe,#dfe6ef)}
.main-nav a{display:block;height:35px;line-height:35px;text-align:center;font-size:13px;font-weight:700;color:#3a3a3a;text-decoration:none;border-right:1px solid #c2ccd9}
.hero-photo{left:8px;top:43px;width:557px;height:296px;background:linear-gradient(160deg,#5f7ea3 0%,#3d5a2e 55%,#2c4a1e 80%)}
.hero-caption{left:8px;top:268px;width:557px;height:71px;background:linear-gradient(rgba(255,255,255,.55),rgba(255,255,255,.95) 40%,#fff)}
.hero-caption p{position:absolute;left:18px;top:12px;width:420px;font-size:19px;font-weight:700;color:#1b58c0;line-height:22px}
.hero-dots{left:561px;top:447px;display:flex;gap:3px}
.hero-dots span{width:19px;height:4px;background:#1b58c0}
.hero-dots span:first-child{background:var(--orange)}
.side-list{left:572px;top:43px;width:327px}
.side-item{position:relative;height:74px;border-bottom:1px solid #fff;background:linear-gradient(#dfe7f2,#cbd7e7)}
.side-thumb{position:absolute;left:7px;top:7px;width:115px;height:60px;background:linear-gradient(135deg,#7a6a40,#2a2a22)}
.side-date{position:absolute;left:131px;top:10px;width:183px;font-size:10px;font-weight:700;color:#4a9ad8;border-bottom:1px solid #8fb8e0;padding-bottom:4px}
.side-text{position:absolute;left:131px;top:32px;width:180px;font-size:10px;line-height:16px;color:#8aa0bc}
.side-arrow{position:absolute;right:8px;bottom:6px;width:0;height:0;border-left:6px solid transparent;border-bottom:6px solid #4a86c8}
/* content */
.content-panel{left:124px;top:480px;width:905px;height:624px;border-radius:8px;background:linear-gradient(#0f3ea0,#0b2f80 60%,#0a2a72);box-shadow:0 0 12px rgba(0,0,0,.4)}
.bar{height:25px;line-height:25px;padding-left:8px;font-size:16px;color:var(--white);border-radius:4px 4px 0 0}
.bar-red{background:linear-gradient(#ff6a30,var(--red-bar))}
.bar-green{background:linear-gradient(#b6e840,var(--green-bar))}
.bar-amber{background:linear-gradient(#ffc040,var(--amber-bar))}
.news-col{top:543px;width:258px}
.news-date{font-size:11px;font-weight:700}
.news-head{margin-top:3px;font-size:11px;font-weight:700;color:var(--orange);line-height:16px}
.news-photo{margin-top:8px;width:258px;height:130px}
.news-body{margin-top:6px;width:210px;font-size:11px;line-height:15px;color:var(--muted)}
.more-btn{width:58px;height:17px;border-radius:4px;background:linear-gradient(#7ed0ff,#2a8ee0);font-size:11px;font-weight:700;text-align:center;line-height:17px}
.section-title{left:145px;top:792px;font-size:16px;line-height:18px}
.section-rule{left:145px;top:812px;width:535px;height:2px;background:var(--sky)}
.mini-story{left:145px;width:260px;height:59px}
.mini-thumb{position:absolute;left:0;top:0;width:78px;height:59px;background:linear-gradient(135deg,#6a5a7a,#2f4a2a)}
.mini-date{position:absolute;left:89px;top:6px;font-size:10px;font-weight:700;color:var(--link)}
.mini-link{position:absolute;left:89px;top:20px;width:140px;font-size:10px;font-weight:700;line-height:16px;color:var(--orange);text-decoration:underline}
.brief-list{left:411px;top:836px;width:269px}
.brief-row{height:29px;display:flex;align-items:center;border-bottom:1px solid rgba(255,255,255,.06);font-size:10px;font-weight:700}
.brief-row .d{width:74px;color:var(--orange)}
.brief-row .l{color:var(--link);text-decoration:underline}
/* contact */
.contact{left:727px;top:503px;width:277px}
.contact-form{height:207px;background:var(--white);color:var(--ink);position:relative;font-size:12px}
.contact-form label{position:absolute;left:12px}
.contact-form .field{position:absolute;left:66px;width:191px;height:18px;border:1px solid #555}
.form-btn{position:absolute;top:179px;width:54px;height:21px;background:linear-gradient(#2f6ad0,#0a3a9a);color:var(--white);font-size:11px;text-align:center;line-height:21px;border:1px solid #0a2a70}
.blog{left:727px;top:751px;width:277px}
.blog-list{margin-top:8px;background:var(--white)}
.blog-row{position:relative;height:60px;border-bottom:1px solid #ddd;background:linear-gradient(#fff,#ececec)}
.blog-avatar{position:absolute;left:7px;top:7px;width:48px;height:46px;background:linear-gradient(#c9946a,#7a4a2a)}
.blog-name{position:absolute;left:63px;top:8px;font-size:10px;font-weight:700;color:#d04a10}
.blog-text{position:absolute;left:63px;top:23px;width:130px;font-size:10px;line-height:16px;color:var(--ink)}
.newsletter{left:728px;top:996px;width:276px;height:73px;border-radius:5px;background:linear-gradient(#3cb0f0,#1a6ad0)}
.newsletter h3{position:absolute;left:11px;top:7px;font-size:19px;font-weight:400}
.newsletter .email{position:absolute;left:15px;top:36px;width:221px;height:23px;background:var(--white);border-radius:4px 0 0 4px;color:#333;font-size:10px;line-height:23px;padding-left:9px}
.newsletter .go{position:absolute;left:236px;top:36px;width:26px;height:23px;background:#eaf4fb;border-radius:0 4px 4px 0;color:#3a8ad0;font-size:12px;font-weight:700;line-height:23px;text-align:center}
/* footer */
.footer-rule{left:123px;width:906px;height:1px;background:rgba(255,255,255,.1)}
.footer-nav{left:0;top:1136px;width:1137px;text-align:center;font-size:11px;color:#1f4a9a;word-spacing:4px}
.copyright{left:0;top:1171px;width:1137px;text-align:center;font-size:11px}
</style>
</head>
<body>
<div class="abs account-bar"></div>
<a class="abs account-link">Creat an Account</a>
<div class="abs login-field" style="left:777px"></div>
<div class="abs login-field" style="left:873px"></div>
<div class="abs login-btn">Login</div>

<div class="abs brand"><span class="brand-mark"></span><span class="brand-name">KESTO</span></div>
<div class="abs call-us">CALL US:123.123.123</div>
<div class="abs social" style="left:924px" aria-label="Social link"></div>
<div class="abs social" style="left:961px" aria-label="Blog link"></div>
<div class="abs social" style="left:998px" aria-label="Social link"></div>

<header class="abs header-panel">
  <nav class="abs main-nav">
    <a style="width:115px">ABOUT US</a><a style="width:103px">ROSTER</a><a style="width:87px">STAFF</a><a style="width:123px">SCHEDULE</a><a style="width:99px">ONLINE</a><a style="width:93px">STORE</a><a style="width:128px">COMMUNITY</a><a style="width:124px;border-right:0">SPONSORS</a>
  </nav>
  <div class="abs hero-photo" role="img" aria-label="Team players cheering together on a field at dusk"></div>
  <div class="abs hero-caption"><p>It is a long established fact that a reader will be distracted.</p></div>
  <div class="abs side-list">
    <div class="side-item"><div class="side-thumb" role="img" aria-label="Team group photo"></div><div class="side-date">SEP 10,2010</div><div class="side-text">It is a long established fact that a distracted by the .</div><span class="side-arrow"></span></div>
    <div class="side-item"><div class="side-thumb" role="img" aria-label="Players posing together"></div><div class="side-date">SEP 10,2010</div><div class="side-text">It is a long established fact that a distracted by the .</div><span class="side-arrow"></span></div>
    <div class="side-item"><div class="side-thumb" role="img" aria-label="Player in a red helmet"></div><div class="side-date">SEP 10,2010</div><div class="side-text">It is a long established fact that a distracted by the .</div><span class="side-arrow"></span></div>
    <div class="side-item"><div class="side-thumb" role="img" aria-label="Player in team jersey"></div><div class="side-date">SEP 10,2010</div><div class="side-text">It is a long established fact that a distracted by the .</div><span class="side-arrow"></span></div>
  </div>
</header>
<div class="abs hero-dots"><span></span><span></span><span></span><span></span></div>

<main class="abs content-panel"></main>
<div class="abs bar bar-red" style="left:145px;top:504px;width:535px">Latest News</div>
<article class="abs news-col" style="left:145px">
  <div class="news-date">SEP 10,2010</div>
  <div class="news-head">It is a long established fact that a reader will be distracted by the .</div>
  <div class="news-photo" role="img" aria-label="Players in yellow jerseys during a scrum" style="background:linear-gradient(#4a5a40,#c8c8a0 60%,#e8e8d8)"></div>
  <p class="news-body">Lorem Ipsum is simply dummy text of the printing and typesetting industry. Lorem Ipsum has been the industry's standard the</p>
</article>
<article class="abs news-col" style="left:421px">
  <div class="news-date">SEP 10,2010</div>
  <div class="news-head">It is a long established fact that a reader will be distracted by the .</div>
  <div class="news-photo" role="img" aria-label="Players in black uniforms on a stadium field" style="background:linear-gradient(#c8d0d8,#7a8a8a 45%,#3a5a30)"></div>
  <p class="news-body">Lorem Ipsum is simply dummy text of the printing and typesetting industry. Lorem Ipsum has been the industry's standard the</p>
</article>
<div class="abs more-btn" style="left:621px;top:779px">more</div>

<div class="abs section-title">In the News</div>
<div class="abs section-rule"></div>
<div class="abs mini-story" style="top:841px"><div class="mini-thumb" role="img" aria-label="Player portrait"></div><div class="mini-date">SEP 10,2010</div><a class="mini-link">It is a long established fact distracted by the .</a></div>
<div class="abs mini-story" style="top:912px"><div class="mini-thumb" role="img" aria-label="Player portrait"></div><div class="mini-date">SEP 10,2010</div><a class="mini-link">It is a long established fact distracted by the .</a></div>
<div class="abs mini-story" style="top:983px"><div class="mini-thumb" role="img" aria-label="Player portrait"></div><div class="mini-date">SEP 10,2010</div><a class="mini-link">It is a long established fact distracted by the .</a></div>
<div class="abs brief-list">
  <div class="brief-row"><span class="d">SEP 10,2010</span><a class="l">It is a long established fact distracted</a></div>
  <div class="brief-row"><span class="d">SEP 10,2010</span><a class="l">It is a long established fact distracted</a></div>
  <div class="brief-row"><span class="d">SEP 10,2010</span><a class="l">It is a long established fact distracted</a></div>
  <div class="brief-row"><span class="d">SEP 10,2010</span><a class="l">It is a long established fact distracted</a></div>
  <div class="brief-row"><span class="d">SEP 10,2010</span><a class="l">It is a long established fact distracted</a></div>
  <div class="brief-row"><span class="d">SEP 10,2010</span><a class="l">It is a long established fact distracted</a></div>
  <div class="brief-row"><span class="d">SEP 10,2010</span><a class="l">It is a long established fact distracted</a></div>
</div>
<div class="abs more-btn" style="left:621px;top:1055px">more</div>

<section class="abs contact">
  <div class="bar bar-green">Contact Us</div>
  <div class="contact-form">
    <label style="top:10px">Name:</label><span class="field" style="top:8px"></span>
    <label style="top:35px">Email:</label><span class="field" style="top:33px"></span>
    <label style="top:60px">Phone:</label><span class="field" style="top:58px"></span>
    <label style="top:85px">Message:</label><span class="field" style="top:84px;height:83px"></span>
    <span class="form-btn" style="left:81px">Sumit</span><span class="form-btn" style="left:138px">Clear</span>
  </div>
</section>

<section class="abs blog">
  <div class="bar bar-amber" style="border-radius:4px">Our Blog</div>
  <div class="blog-list">
    <div class="blog-row"><div class="blog-avatar" role="img" aria-label="Blogger portrait"></div><div class="blog-name">Jenney</div><div class="blog-text">It is a long established fact distracted by the .</div></div>
    <div class="blog-row"><div class="blog-avatar" role="img" aria-label="Blogger portrait"></div><div class="blog-name">Jhone</div><div class="blog-text">It is a long established fact distracted by the .</div></div>
    <div class="blog-row"><div class="blog-avatar" role="img" aria-label="Blogger portrait"></div><div class="blog-name">Jesica</div><div class="blog-text">It is a long established fact distracted by the .</div></div>
  </div>
</section>

<section class="abs newsletter">
  <h3>Newsletter</h3>
  <div class="email">Enter your e-mail please</div>
  <div class="go">Go</div>
</section>

<div class="abs footer-rule" style="top:1127px"></div>
<nav class="abs footer-nav">ABOUT US ROSTER STAFF SCHEDULE ONLINE STORE COMMUNITY SPONSORS</nav>
<div class="abs footer-rule" style="top:1160px"></div>
<div class="abs copyright">Copyright © 2010 KESTO woman football .</div>
</body>
</html>
```